Vitamin and Nutrition Ecommerce Site Needs a High End Website Design

We need a new and improved Homepage design for a leading Vitamin eCommerce business.
We supply our customers worldwide with leading brands of vitamin supplements and nutritional products at discounted prices.
The site design and layout must improve sales conversion and maximize the user experience staying on the site!

We will need to see;
A New Nutri Harbour stylized font (no logo)
High-End Modern Design
Easy Sales Conversion Experience
Excellent Layout, Fast Navigation
Quality Font style, Stylish Colour Palette Selection
Appropriate Spacing
Call To Action to Improve Sales Conversion
Web page should Look Clean and Minimalist

The design should improve sales, communicate easy to find products, facilitate fast ordering, have a modern and professional appearance centered toward a predominately female consumer.

Thank you for your interest in this project!

Current design can be found on this link;
www.nutriharbour.com.au/nutri/

Target Market(s)

80% Female 30-65 years

Industry/Entity Type

Business

Number of Pages Required

1 page

Colors

Designer to choose colors to be used in the design.

Requirements
Must have
• design must result improve sales conversion
• new Nutri Harbour font design
• search field
• attractive clean modern design
• stylish font and colour palette selection
Nice to have
• white background
Should not have
• cluttered or busy layout
• confusing navigation

```html
<!DOCTYPE html>
<html lang="en">
<head>
<meta charset="utf-8">
<title>Nutri Harbour – Home</title>
<link href="https://fonts.googleapis.com/css2?family=Roboto:wght@300;400;500;700&display=swap" rel="stylesheet">
<style>
:root{
  --brown:#5b4a45;
  --brown-dark:#4d3e3a;
  --green:#74d1a3;
  --green-soft:#8fd9b3;
  --grey-bg:#f0f0f0;
  --grey-card:#f3f3f3;
  --text:#555;
  --white:#fff;
}
*{box-sizing:border-box;margin:0;padding:0}
html,body{width:1200px;height:2990px;overflow:hidden}
body{position:relative;font-family:'Roboto',sans-serif;color:var(--text);background:var(--white)}
.abs{position:absolute}
a{color:inherit;text-decoration:none}

/* header */
.header{position:absolute;left:0;top:0;width:1200px;height:114px;background:linear-gradient(#ececec,#f7f7f7)}
.utility{position:absolute;left:160px;top:9px;font-size:9px;color:#9a9a9a;display:flex;gap:14px;letter-spacing:.3px}
.search{position:absolute;left:790px;top:4px;width:166px;height:24px;background:#fff;border:1px solid #ddd;font-size:9px;color:#aaa;padding:6px 8px}
.search-btn{position:absolute;right:-1px;top:-1px;width:24px;height:24px;background:var(--brown)}
.cart-label{position:absolute;left:972px;top:10px;font-size:9px;color:#888}
.cart-icon{position:absolute;left:1012px;top:4px}
.brand{font-family:'Roboto',sans-serif;font-weight:500;color:var(--brown);white-space:nowrap;display:flex;align-items:center;gap:10px}
.brand .dot{width:14px;height:14px;border-radius:50%;background:var(--green)}
.header .brand{position:absolute;left:162px;top:50px;font-size:38px}
.phone{position:absolute;left:826px;top:56px;display:flex;align-items:center;gap:8px;font-size:26px;font-weight:700;color:#333}
.nav{position:absolute;left:0;top:114px;width:1200px;height:40px;background:var(--brown);display:flex;align-items:center;padding-left:160px;gap:17px;font-size:11px;color:var(--white);font-weight:500}

/* hero */
.hero{position:absolute;left:0;top:154px;width:1200px;height:474px;overflow:hidden;
  background:
    radial-gradient(ellipse 300px 200px at 250px 130px,#e8b995 0%,rgba(232,185,149,0) 100%),
    radial-gradient(ellipse 260px 220px at 430px 250px,#e3b08c 0%,rgba(227,176,140,0) 100%),
    radial-gradient(ellipse 260px 160px at 150px 360px,#fbfbfb 0%,rgba(251,251,251,0) 100%),
    radial-gradient(ellipse 180px 140px at 200px 70px,#c9874f 0%,rgba(201,135,79,0) 100%),
    linear-gradient(90deg,#dfe6ee,#f3f6fa 55%,#dce6f0)}
.hero-people{position:absolute;left:0;top:0;width:620px;height:474px}
.hero-products{position:absolute;left:576px;top:130px;width:520px;height:330px;
  background:
    radial-gradient(ellipse 200px 60px at 260px 30px,#f3e07a 0%,rgba(243,224,122,0) 100%),
    radial-gradient(ellipse 260px 110px at 260px 210px,#4fae5c 0%,rgba(79,174,92,0) 100%),
    radial-gradient(ellipse 240px 130px at 260px 160px,#f4f6ee 0%,rgba(244,246,238,0) 100%)}
.hero .brand{position:absolute;left:700px;top:40px;font-size:36px}

/* category tiles */
.tile{position:absolute;top:658px;width:270px;height:180px;overflow:hidden}
.tile-title{position:absolute;font-size:16px;font-weight:700;color:#444}
.btn-outline{position:absolute;width:88px;height:28px;border:1px solid #444;font-size:9px;display:flex;align-items:center;justify-content:center;color:#444}
.tile-dark .tile-title{color:#fff}
.tile-dark .btn-outline{border-color:#fff;color:#fff}

/* welcome */
.welcome-frame{position:absolute;left:162px;top:886px;width:290px;height:334px;background:var(--green)}
.welcome-frame .inner{position:absolute;left:18px;top:18px;width:240px;height:290px;border:1px solid rgba(255,255,255,.7)}
.welcome-photo{position:absolute;left:208px;top:926px;width:294px;height:334px;
  background:
    radial-gradient(ellipse 90px 110px at 120px 110px,#e9c3a6 0%,rgba(233,195,166,0) 100%),
    radial-gradient(ellipse 130px 160px at 110px 110px,#c98a52 0%,rgba(201,138,82,0) 100%),
    radial-gradient(ellipse 50px 90px at 230px 190px,#f7f7f4 0%,rgba(247,247,244,0) 100%),
    radial-gradient(ellipse 150px 90px at 120px 320px,#e8a7a0 0%,rgba(232,167,160,0) 100%),
    linear-gradient(160deg,#eef0ec,#e7e5df)}
.welcome-title{position:absolute;left:560px;top:882px;font-size:32px;font-weight:300;color:#444}
.welcome-title b{font-weight:700}
.title-rule{position:absolute;height:2px;background:var(--green)}
.copy{position:absolute;left:560px;width:482px;font-size:11px;line-height:17px;color:#555}
.btn-dark{position:absolute;background:var(--brown);color:#fff;font-size:11px;font-weight:500;display:flex;align-items:center;justify-content:center}

/* on sale */
.sale{position:absolute;left:0;top:1320px;width:1200px;height:446px;
  background:
    radial-gradient(ellipse 200px 260px at 1060px 220px,#8c7870 0%,rgba(140,120,112,0) 100%),
    radial-gradient(ellipse 160px 200px at 900px 160px,#86716a 0%,rgba(134,113,106,0) 100%),
    repeating-linear-gradient(0deg,#6f5d56 0 28px,#6a5852 28px 30px),
    #6b5953}
.sale-title{position:absolute;left:0;top:1354px;width:1200px;text-align:center;font-size:36px;font-weight:700;color:#fff}
.sale-line{position:absolute;top:1378px;height:1px;background:rgba(255,255,255,.35)}
.sale-card{position:absolute;top:1446px;width:198px;height:270px;background:#fff;text-align:center}
.sale-card .img{position:absolute;left:34px;top:18px;width:130px;height:126px}
.sale-card .name{position:absolute;left:0;top:158px;width:100%;font-size:12px;line-height:16px;color:#444;padding:0 20px}
.sale-card .price{position:absolute;left:0;top:196px;width:100%;font-size:16px;font-weight:700;color:#333}
.btn-green{position:absolute;background:var(--green);color:#2d3a33;font-size:9px;font-weight:500;display:flex;align-items:center;justify-content:center}
.sale-card .btn-green{left:57px;top:226px;width:84px;height:26px}

/* new arrivals */
.section-title{position:absolute;left:0;width:1200px;text-align:center;font-size:34px;font-weight:700;color:var(--brown)}
.arrival{position:absolute;top:1906px;width:202px}
.arrival .img-wrap{height:204px;background:var(--grey-card);position:relative}
.arrival .img{position:absolute;left:36px;top:20px;width:130px;height:170px}
.arrival .desc{height:62px;background:var(--green-soft);font-size:11px;color:#fff;text-align:center;padding:16px 18px;line-height:14px}
.arrival .shop{height:38px;background:var(--brown);color:#fff;font-size:13px;font-weight:700;display:flex;align-items:center;justify-content:center;gap:6px}
.slider-arrow{position:absolute;width:48px;height:48px;border-radius:50%;background:#ddd;display:flex;align-items:center;justify-content:center}

/* testimonial */
.testimonial{position:absolute;left:0;top:2264px;width:1200px;height:282px;
  background:
    radial-gradient(ellipse 220px 200px at 260px 140px,#a6dcc0 0%,rgba(166,220,192,0) 100%),
    radial-gradient(ellipse 160px 200px at 1060px 140px,#9ddbbb 0%,rgba(157,219,187,0) 100%),
    linear-gradient(90deg,#7fcfa5,#86d5ad 50%,#7fcfa5)}
.avatar{position:absolute;left:548px;top:2288px;width:104px;height:104px;border-radius:50%;border:4px solid #fff;
  background:radial-gradient(ellipse 30px 38px at 50% 42%,#e5c2a6 0%,rgba(229,194,166,0) 100%),linear-gradient(#6d5a4c 0%,#e6e2dd 55%,#f4f4f4)}
.quote{position:absolute;left:196px;top:2418px;width:808px;font-size:11px;line-height:18px;color:#fff;text-align:center}
.author{position:absolute;left:0;top:2488px;width:1200px;text-align:center;font-size:14px;color:#3f4a44}
.t-arrow{position:absolute;top:2408px;width:40px;height:40px;border-radius:50%;background:rgba(70,70,70,.45);display:flex;align-items:center;justify-content:center}

/* features */
.features{position:absolute;left:0;top:2546px;width:1200px;height:130px;background:var(--grey-bg)}
.feature{position:absolute;top:2580px;display:flex;align-items:center;gap:12px}
.feature .ic{width:60px;height:60px;border-radius:50%;border:2px solid #444;display:flex;align-items:center;justify-content:center}
.feature .t1{font-size:14px;font-weight:700;color:#444}
.feature .t2{font-size:10px;color:#777}

/* footer */
.foot-h{position:absolute;top:2712px;font-size:13px;font-weight:700;color:#444}
.footer .brand{position:absolute;left:162px;top:2752px;font-size:32px}
.foot-copy{position:absolute;font-size:10px;line-height:17px;color:#777}
.links{position:absolute;top:2762px;list-style:none;font-size:10px;color:#555}
.links li{height:27px}
.links li::before{content:"›";margin-right:8px;color:#777}
.email{position:absolute;left:840px;top:2808px;width:200px;height:34px;border:2px solid var(--brown);font-size:10px;padding:10px;color:#666}
.bottom{position:absolute;left:0;top:2948px;width:1200px;height:42px;background:var(--brown)}
.bottom .copy-r{position:absolute;left:162px;top:14px;font-size:10px;color:#fff}
.pay{position:absolute;top:11px;width:28px;height:18px;background:#fff;border-radius:2px}
.social{position:absolute;top:8px;width:26px;height:26px;border-radius:50%;border:1px solid #fff}
</style>
</head>
<body>

<header class="header">
  <nav class="utility"><a>MY ACCOUNT</a><a>MY WISHLIST</a><a>MY CART</a><a>CHECKOUT</a><a>REGISTER</a><a>LOG IN</a></nav>
  <div class="search">SEARCH HERE...
    <div class="search-btn"><svg width="24" height="24" viewBox="0 0 24 24"><circle cx="11" cy="11" r="4" fill="none" stroke="#fff" stroke-width="1.6"/><line x1="14" y1="14" x2="17" y2="17" stroke="#fff" stroke-width="1.6"/></svg></div>
  </div>
  <div class="cart-label">CART</div>
  <svg class="cart-icon" width="30" height="24" viewBox="0 0 30 24"><path d="M3 8h3l3 9h9l3-7H8" fill="none" stroke="#74d1a3" stroke-width="2"/><circle cx="11" cy="20" r="1.6" fill="#74d1a3"/><circle cx="17" cy="20" r="1.6" fill="#74d1a3"/><circle cx="23" cy="6" r="5" fill="#74d1a3"/><text x="23" y="8.5" font-size="7" text-anchor="middle" fill="#fff" font-family="Roboto,sans-serif">0</text></svg>
  <div class="brand"><span class="dot"></span>Nutri Harbour</div>
  <div class="phone">
    <svg width="34" height="34" viewBox="0 0 34 34"><circle cx="17" cy="17" r="15" fill="none" stroke="#333" stroke-width="2"/><rect x="12" y="8" width="10" height="18" rx="2" fill="none" stroke="#333" stroke-width="2"/><line x1="15" y1="23" x2="19" y2="23" stroke="#333" stroke-width="1.5"/></svg>
    1-800-555-0142
  </div>
</header>

<nav class="nav">
  <a>HOME</a><a>BRAND</a><a>SUPPLEMENTS</a><a>SPORTS NUTRITION</a><a>HAIRCARE</a><a>CHIROPRACTIC PILLOWS</a><a>HEALTH CONDITION</a><a>BEAUTY &amp; SKINCARE</a><a>GLUTEN FREE</a><a>ON SALE</a>
</nav>

<section class="hero">
  <div class="hero-people" role="img" aria-label="Smiling mature couple embracing"></div>
  <div class="brand"><span class="dot"></span>Nutri Harbour</div>
  <div class="hero-products" role="img" aria-label="Pyramid of vitamin supplement bottles with yellow lids and green labels"></div>
</section>

<section>
  <div class="tile" style="left:162px;background:linear-gradient(90deg,#9acd62 0%,#d9e69a 40%,#f4f2b0 60%,#f6f3b2)">
    <div class="abs" role="img" aria-label="Woman with clear skin" style="left:0;top:0;width:160px;height:180px;background:radial-gradient(ellipse 60px 80px at 100px 90px,#efd2bd 0%,rgba(239,210,189,0) 100%),radial-gradient(ellipse 70px 100px at 110px 80px,#8a5a3b 0%,rgba(138,90,59,0) 100%),linear-gradient(90deg,#86c04f,#bcd98a)"></div>
    <div class="tile-title" style="left:160px;top:56px">SKINCARE</div>
    <div class="btn-outline" style="left:158px;top:114px">READ MORE</div>
  </div>
  <div class="tile tile-dark" style="left:466px;background:linear-gradient(90deg,#8f9b94,#a8a395 50%,#b79a7c)">
    <div class="abs" role="img" aria-label="Woman with long wavy hair" style="left:90px;top:0;width:180px;height:180px;background:radial-gradient(ellipse 40px 55px at 110px 80px,#f0cdb5 0%,rgba(240,205,181,0) 100%),radial-gradient(ellipse 90px 100px at 90px 100px,#b06c3a 0%,rgba(176,108,58,0) 100%)"></div>
    <div class="tile-title" style="left:16px;top:56px">HAIRCARE</div>
    <div class="btn-outline" style="left:14px;top:114px">READ MORE</div>
  </div>
  <div class="tile tile-dark" style="left:770px;background:#6e625e">
    <div class="abs" role="img" aria-label="Coffee bag and product box" style="left:160px;top:0;width:110px;height:180px;background:radial-gradient(ellipse 30px 40px at 85px 130px,#c48a45 0%,rgba(196,138,69,0) 100%),linear-gradient(90deg,#2a2523,#3b3330 60%,#6e625e)"></div>
    <div class="tile-title" style="left:14px;top:50px;line-height:19px">EXCLUSIVE<br>OFFERS</div>
    <div class="btn-outline" style="left:14px;top:110px">READ MORE</div>
  </div>
</section>

<section>
  <div class="welcome-frame"><div class="inner"></div></div>
  <div class="welcome-photo" role="img" aria-label="Smiling woman holding a supplement bottle"></div>
  <h1 class="welcome-title">Welcome to Nutri <b>Harbour</b></h1>
  <div class="title-rule" style="left:560px;top:922px;width:100px"></div>
  <p class="copy" style="top:952px">Lorem Ipsum is simply dummy text of the printing and typesetting industry. Lorem Ipsum has been the industry's standard dummy text ever since the 1500s, when an unknown printer took a galley of type and scrambled it to make a type specimen book. It has survived not only five centuries, but also the leap into electronic typesetting, remaining essentially unchanged. It was popularised in the 1960s with the release of Letraset sheets containing Lorem Ipsum passages, and more recently with desktop publishing software like Aldus PageMaker including versions of Lorem Ipsum</p>
  <p class="copy" style="top:1066px">Lorem Ipsum is simply dummy text of the printing and typesetting industry. Lorem Ipsum has been the industry's standard dummy text ever since the 1500s, when an unknown printer took a galley of type and scrambled it to make a type specimen book. It has survived not only five centuries, but also the leap into electronic typesetting, remaining essentially unchanged. It was popularised in the 1960s with the release of Letraset sheets containing Lorem Ipsum passages, and more recently with desktop publishing software like Aldus PageMaker including versions of Lorem Ipsum</p>
  <div class="btn-dark" style="left:562px;top:1212px;width:114px;height:36px">READ MORE &nbsp;+</div>
  <div class="brand abs" style="left:822px;top:1208px;font-size:32px"><span class="dot"></span>Nutri Harbour</div>
</section>

<section>
  <div class="sale" role="img" aria-label="Faded photo of a couple outdoors beside a brick wall"></div>
  <div class="sale-line" style="left:162px;width:340px"></div>
  <div class="sale-line" style="left:698px;width:340px"></div>
  <h2 class="sale-title">On Sale</h2>
  <div class="sale-card" style="left:162px"><div class="img" role="img" aria-label="Three brown supplement jars" style="background:radial-gradient(ellipse 60px 50px at 50% 60%,#5a4232 0%,rgba(90,66,50,0) 100%),radial-gradient(ellipse 50px 20px at 50% 28%,#b9a27c 0%,rgba(185,162,124,0) 100%)"></div><div class="name">Acne control tablets extra strength new</div><div class="price">$13.95</div><div class="btn-green">ADD TO CART</div></div>
  <div class="sale-card" style="left:390px"><div class="img" role="img" aria-label="Amber supplement bottle" style="background:radial-gradient(ellipse 28px 60px at 50% 55%,#5a2a16 0%,rgba(90,42,22,0) 100%),radial-gradient(ellipse 22px 12px at 50% 12%,#1f1a18 0%,rgba(31,26,24,0) 100%)"></div><div class="name">Acne control tablets extra strength new</div><div class="price">$13.95</div><div class="btn-green">ADD TO CART</div></div>
  <div class="sale-card" style="left:616px"><div class="img" role="img" aria-label="White tub with green label" style="background:radial-gradient(ellipse 50px 30px at 50% 45%,#39a96b 0%,rgba(57,169,107,0) 100%),radial-gradient(ellipse 60px 58px at 50% 52%,#eef2ee 0%,rgba(238,242,238,0) 100%)"></div><div class="name">Acne control tablets extra strength new</div><div class="price">$13.95</div><div class="btn-green">ADD TO CART</div></div>
  <div class="sale-card" style="left:842px"><div class="img" role="img" aria-label="Coffee bag and box" style="background:radial-gradient(ellipse 24px 28px at 65% 70%,#c48a45 0%,rgba(196,138,69,0) 100%),radial-gradient(ellipse 36px 62px at 42% 50%,#2c2522 0%,rgba(44,37,34,0) 100%)"></div><div class="name">Acne control tablets extra strength new</div><div class="price">$13.95</div><div class="btn-green">ADD TO CART</div></div>
</section>

<section>
  <h2 class="section-title" style="top:1808px">NEW ARRIVALS</h2>
  <div class="title-rule" style="left:580px;top:1858px;width:40px"></div>
  <div class="slider-arrow" style="left:84px;top:2032px"><svg width="14" height="14" viewBox="0 0 14 14"><path d="M9 2L4 7l5 5" fill="none" stroke="#555" stroke-width="2"/></svg></div>
  <div class="slider-arrow" style="left:1070px;top:2032px"><svg width="14" height="14" viewBox="0 0 14 14"><path d="M5 2l5 5-5 5" fill="none" stroke="#555" stroke-width="2"/></svg></div>
  <div class="arrival" style="left:162px"><div class="img-wrap"><div class="img" role="img" aria-label="White supplement bottle with blue label" style="background:radial-gradient(ellipse 30px 22px at 50% 55%,#8fb0d8 0%,rgba(143,176,216,0) 100%),radial-gradient(ellipse 40px 70px at 50% 52%,#ffffff 0%,rgba(255,255,255,0) 100%)"></div></div><div class="desc">Lorem Ipsum is simply dummy ting industry</div><div class="shop">SHOP NOW <svg width="12" height="12" viewBox="0 0 12 12"><circle cx="6" cy="6" r="5" fill="none" stroke="#fff" stroke-width="1.4"/><path d="M5 4l2 2-2 2" fill="none" stroke="#fff" stroke-width="1.4"/></svg></div></div>
  <div class="arrival" style="left:386px"><div class="img-wrap"><div class="img" role="img" aria-label="Amber supplement bottle" style="background:radial-gradient(ellipse 30px 70px at 50% 55%,#6a3220 0%,rgba(106,50,32,0) 100%),radial-gradient(ellipse 26px 12px at 50% 12%,#1f1a18 0%,rgba(31,26,24,0) 100%)"></div></div><div class="desc">Lorem Ipsum is simply dummy ting industry</div><div class="shop">SHOP NOW <svg width="12" height="12" viewBox="0 0 12 12"><circle cx="6" cy="6" r="5" fill="none" stroke="#fff" stroke-width="1.4"/><path d="M5 4l2 2-2 2" fill="none" stroke="#fff" stroke-width="1.4"/></svg></div></div>
  <div class="arrival" style="left:612px"><div class="img-wrap"><div class="img" role="img" aria-label="White fibre supplement bottle with capsules" style="background:radial-gradient(ellipse 30px 12px at 50% 88%,#c7b27a 0%,rgba(199,178,122,0) 100%),radial-gradient(ellipse 26px 20px at 50% 45%,#7fb26a 0%,rgba(127,178,106,0) 100%),radial-gradient(ellipse 38px 66px at 50% 45%,#ffffff 0%,rgba(255,255,255,0) 100%)"></div></div><div class="desc">Lorem Ipsum is simply dummy ting industry</div><div class="shop">SHOP NOW <svg width="12" height="12" viewBox="0 0 12 12"><circle cx="6" cy="6" r="5" fill="none" stroke="#fff" stroke-width="1.4"/><path d="M5 4l2 2-2 2" fill="none" stroke="#fff" stroke-width="1.4"/></svg></div></div>
  <div class="arrival" style="left:838px"><div class="img-wrap"><div class="img" role="img" aria-label="Black jar with yellow label" style="background:radial-gradient(ellipse 22px 26px at 50% 55%,#d9c84a 0%,rgba(217,200,74,0) 100%),radial-gradient(ellipse 58px 72px at 50% 52%,#1d1d1d 0%,rgba(29,29,29,0) 100%)"></div></div><div class="desc">Lorem Ipsum is simply dummy ting industry</div><div class="shop">SHOP NOW <svg width="12" height="12" viewBox="0 0 12 12"><circle cx="6" cy="6" r="5" fill="none" stroke="#fff" stroke-width="1.4"/><path d="M5 4l2 2-2 2" fill="none" stroke="#fff" stroke-width="1.4"/></svg></div></div>
</section>

<section>
  <div class="testimonial" role="img" aria-label="Faded portrait of a smiling woman on green"></div>
  <div class="avatar" role="img" aria-label="Customer portrait"></div>
  <div class="t-arrow" style="left:122px"><svg width="12" height="12" viewBox="0 0 12 12"><path d="M8 2L4 6l4 4" fill="none" stroke="#fff" stroke-width="2"/></svg></div>
  <div class="t-arrow" style="left:1034px"><svg width="12" height="12" viewBox="0 0 12 12"><path d="M4 2l4 4-4 4" fill="none" stroke="#fff" stroke-width="2"/></svg></div>
  <p class="quote">Lorem Ipsum is simply dummy text of the printing and typesetting industry. Lorem Ipsum has been the industry's standard dummy text ever since the 1500s, when an unknown printer took a galley of type and scrambled it to make a type specimen book. It has survived not only five centuries, but also the leap into electronic typesetting, remaining essentially unchanged</p>
  <div class="author">Daniel | Denver, CO</div>
</section>

<section>
  <div class="features"></div>
  <div class="feature" style="left:162px"><div class="ic"><svg width="34" height="24" viewBox="0 0 34 24"><rect x="2" y="4" width="18" height="12" fill="#444"/><path d="M20 8h6l4 4v4H20z" fill="#444"/><circle cx="8" cy="19" r="3" fill="#444"/><circle cx="25" cy="19" r="3" fill="#444"/></svg></div><div><div class="t1">FREE SHIPPING &amp; RETURN</div><div class="t2">for all orders over $99</div></div></div>
  <div class="feature" style="left:410px"><div class="ic"><svg width="30" height="30" viewBox="0 0 30 30"><circle cx="12" cy="6" r="3" fill="#444"/><path d="M12 10v10l-4 8M12 20l4 8M12 13l-5 4M12 13h6" fill="none" stroke="#444" stroke-width="2.5"/><rect x="18" y="14" width="8" height="12" fill="#444"/></svg></div><div><div class="t1">OFFICIAL STOCKIST</div><div class="t2">of more than 100 brands</div></div></div>
  <div class="feature" style="left:618px"><div class="ic"><svg width="30" height="30" viewBox="0 0 30 30"><path d="M8 24a6 6 0 0 1 0-8l9-9a6 6 0 0 1 8 8l-9 9a6 6 0 0 1-8 0z" fill="none" stroke="#444" stroke-width="2.5"/><path d="M12 12l8 8" stroke="#444" stroke-width="2.5"/></svg></div><div><div class="t1">2 FREE SAMPLES</div><div class="t2">on all orders over $99</div></div></div>
  <div class="feature" style="left:812px"><div class="ic"><svg width="26" height="26" viewBox="0 0 26 26"><path d="M6 3l16 10L6 23z" fill="none" stroke="#444" stroke-width="2.5" stroke-linejoin="round"/></svg></div><div><div class="t1">VERIFIED TRUSTED STORE</div><div class="t2">RATING OF 4.9/5</div></div></div>
</section>

<footer class="footer">
  <div class="foot-h" style="left:162px">SHORTLY ABOUT US</div>
  <div class="brand"><span class="dot"></span>Nutri Harbour</div>
  <p class="foot-copy" style="left:162px;top:2806px;width:204px">Lorem Ipsum is simply dummy text the printing and typesetting industry. Lorem Ipsum has been the industry's standard an unknown printer took a galley of type and scrambled it to make a type specimen book.</p>
  <div class="foot-h" style="left:454px">QUICK LINKS</div>
  <ul class="links" style="left:454px"><li>HOME</li><li>BRAND</li><li>SUPPLEMENTS</li><li>SPORTS NUTRITION</li><li>HAIRCARE</li></ul>
  <ul class="links" style="left:636px;top:2736px"><li>CHIROPRACTIC PILLOWS</li><li>CHIROPRACTIC PILLOWS</li><li>BEAUTY &amp; SKINCARE</li><li>GLUTEN FREE</li><li>ON SALE</li></ul>
  <div class="foot-h" style="left:840px">JOIN NUTRI HARBOUR REWARDS</div>
  <p class="foot-copy" style="left:840px;top:2740px;width:210px">Be rewarded with exclusive member offers, including discounts, sales, freebies, gifts with purchase and competitions.</p>
  <div class="email">your email</div>
  <div class="btn-green" style="left:840px;top:2860px;width:98px;height:34px;font-size:11px">SUBSCRIBE</div>
  <div class="bottom">
    <div class="copy-r">© 2017 All Rights Reserved</div>
    <div class="pay" style="left:530px"></div>
    <div class="pay" style="left:562px"></div>
    <div class="pay" style="left:594px"></div>
    <div class="pay" style="left:626px"></div>
    <div class="social" style="left:904px"></div>
    <div class="social" style="left:940px"></div>
    <div class="social" style="left:976px"></div>
    <div class="social" style="left:1012px"></div>
  </div>
</footer>

</body>
</html>
```